Business cards design for T38 (Разработка визитных карточек)

We would like to get design of our business cards loosely based on our website design [url removed, login to view]

logo in vector is atteched

There should be following info to be present on business card:
Martin Colvey
CEO
T38
+7 (222) 222-22-22
+7 (222) 222-22-22
colvey@tessarine-mail.ru
222222, Moscow, Ulitsa Tikhvoronskaya, 7B

```html
<!DOCTYPE html>
<html lang="en">
<head>
<meta charset="utf-8">
<title>T38 — Business Cards</title>
<link rel="stylesheet" href="https://fonts.googleapis.com/css2?family=Open+Sans:wght@400;700&display=swap">
<style>
  :root {
    --backdrop: #8c8c8c;
    --red: #d41f26;
    --red-dark: #a8141b;
    --white: #ffffff;
    --steel-light: #ededed;
    --steel-mid: #c4c4c4;
  }
  html, body {
    margin: 0;
    width: 1200px;
    height: 800px;
    overflow: hidden;
    background: var(--backdrop);
  }
  .sheet {
    width: 1200px;
    height: 800px;
    display: flex;
    flex-direction: column;
    align-items: center;
    justify-content: center;
    gap: 40px;
  }
  .card {
    width: 620px;
    height: 344px;
    display: block;
    box-shadow: 0 6px 18px rgba(0,0,0,0.3);
  }
  .card text { font-family: "Open Sans", Arial, sans-serif; }
  .logo-word { font-weight: 700; }
  .contact { fill: var(--white); font-size: 15px; }
  .person { fill: var(--white); font-size: 17px; }
</style>
</head>
<body>
<main class="sheet">

  <svg class="card card-back" viewBox="0 0 620 344" aria-label="T38 business card, back side">
    <defs>
      <linearGradient id="redFace" x1="0" y1="0" x2="1" y2="1">
        <stop offset="0" stop-color="var(--red-dark)"/>
        <stop offset="0.5" stop-color="var(--red)"/>
        <stop offset="1" stop-color="var(--red-dark)"/>
      </linearGradient>
    </defs>
    <rect width="620" height="344" fill="url(#redFace)"/>
    <text class="logo-word" x="165" y="168" font-size="68" fill="var(--white)">T38</text>
    <text x="167" y="200" font-size="13" fill="var(--white)">222222, Moscow, Ulitsa Tikhvoronskaya, 7B</text>
  </svg>

  <svg class="card card-front" viewBox="0 0 620 344" aria-label="T38 business card, front side">
    <defs>
      <linearGradient id="redFront" x1="0" y1="0" x2="1" y2="1">
        <stop offset="0" stop-color="var(--red-dark)"/>
        <stop offset="0.55" stop-color="var(--red)"/>
        <stop offset="1" stop-color="var(--red-dark)"/>
      </linearGradient>
      <radialGradient id="steelArea" cx="0.5" cy="0.5" r="0.5">
        <stop offset="0" stop-color="var(--steel-light)"/>
        <stop offset="1" stop-color="var(--steel-mid)"/>
      </radialGradient>
      <clipPath id="cardEdge"><rect width="620" height="344"/></clipPath>
    </defs>
    <rect width="620" height="344" fill="url(#redFront)"/>

    <g clip-path="url(#cardEdge)">
      <circle class="dial-area" cx="190" cy="350" r="215" fill="url(#steelArea)"
              role="img" aria-label="Brushed metal dial illustration with a dark ring, red stars and a pointer"/>
    </g>
    <text class="logo-word" x="190" y="300" font-size="54" text-anchor="middle" fill="var(--red)">T38</text>

    <g class="details" text-anchor="end">
      <text class="person" x="590" y="62">Martin Colvey</text>
      <text class="person" x="590" y="84">CEO</text>
      <text class="contact" x="590" y="156">+7 (222) 222-22-22</text>
      <text class="contact" x="590" y="174">+7 (222) 222-22-22</text>
      <text class="contact" x="590" y="192">colvey@tessarine-mail.ru</text>
      <text class="contact" x="590" y="210">www.tessarine-mail.ru</text>
    </g>
  </svg>

</main>
</body>
</html>
```